Super elegant, crisp & clean Business card design required

We recently upgraded our branding - which is on our website - tavorelstudio.com

I would like a simple, yet elegant, clean business card design please.

The font of my logo is Cinzel - and because of the natural colour - it's best to have this on a black background.

I would like to have the back of the business card - with simply my logo.

PLEASE DO NOT SUBMIT A COMPLICATED / UNCLEAN DESIGN

Industry/Entity Type

Business

Contact Information for Business Card

Dalvik Ostrander Photography

Font styles to use
Other font styles liked:
• Cinzel

Requirements
Must have
• A backpage with nothing but my logo
• Simple design - stands out
Should not have
• Colour that dont align with my logo
• Over complicated '/ non symmetrical design

```html
<!DOCTYPE html>
<html lang="en">
<head>
<meta charset="utf-8">
<title>Dalvik Ostrander Photography – Business Card</title>
<link href="https://fonts.googleapis.com/css2?family=Cinzel:wght@400;700&family=Source+Sans+3:wght@400&display=swap" rel="stylesheet">
<style>
  :root {
    --stage: #141414;
    --card-white: #ffffff;
    --band: #85745a;
    --card-back: #7b6a4e;
    --brand-ink: #7a6749;
    --body-ink: #333333;
    --light-ink: #ffffff;
  }
  * { margin: 0; padding: 0; box-sizing: border-box; }
  html, body { width: 1200px; height: 900px; overflow: hidden; background: var(--stage); }
  .canvas { position: relative; width: 1200px; height: 900px; }
  .card { position: absolute; top: 170px; width: 347px; height: 561px; overflow: hidden; }
  .card-front { left: 259px; background: var(--card-white); }
  .card-back { left: 631px; background: var(--card-back); }

  .front-frame { position: absolute; inset: 0; }

  .front-mark {
    position: absolute; top: 138px; left: 0; width: 100%;
    text-align: center; font-family: "Cinzel", serif; font-weight: 400;
    font-size: 22px; letter-spacing: 1px; line-height: 1.3; color: var(--brand-ink);
  }

  .contact { position: absolute; top: 314px; left: 0; width: 100%; text-align: center;
    font-family: "Source Sans 3", sans-serif; color: var(--body-ink); }
  .contact-name { font-family: "Cinzel", serif; font-weight: 700; font-size: 25px;
    color: var(--brand-ink); line-height: 1; letter-spacing: .5px; }
  .contact-role { font-size: 15px; margin-top: 5px; }
  .contact-lines { margin-top: 22px; font-size: 15px; line-height: 20.5px; }
  .contact-address { margin-top: 14px; font-size: 15px; line-height: 17px; }

  .back-badge { position: absolute; top: 203px; left: 50%; width: 60px; height: 60px;
    margin-left: -30px; border: 2px solid var(--light-ink); border-radius: 50%; }
  .back-wordmark { position: absolute; top: 330px; left: 0; width: 100%; text-align: center;
    font-family: "Cinzel", serif; font-weight: 400; color: var(--light-ink);
    font-size: 23px; line-height: 1.1; letter-spacing: .5px; }
  .back-wordmark .line-small { display: block; font-size: 12px; letter-spacing: 6px; margin-top: 3px; }
  .back-web { position: absolute; top: 466px; left: 0; width: 100%; text-align: center;
    font-family: "Source Sans 3", sans-serif; font-size: 16px; color: var(--light-ink); }
</style>
</head>
<body>
<main class="canvas">
  <section class="card card-front" aria-label="Card front">
    <svg class="front-frame" width="347" height="561" viewBox="0 0 347 561" aria-hidden="true">
      <rect x="0" y="0" width="347" height="30" fill="#85745a"/>
      <polygon points="134,30 211,30 172.5,68" fill="#85745a"/>
      <rect x="0" y="533" width="347" height="28" fill="#85745a"/>
    </svg>
    <div class="front-mark">Dalvik Ostrander</div>
    <div class="contact">
      <p class="contact-name">ROWAN HALE</p>
      <p class="contact-role">Managing Director</p>
      <div class="contact-lines">
        <p>823-456-7890</p>
        <p>823-456-7890</p>
        <p>info@youremail.com</p>
      </div>
      <div class="contact-address">
        <p>1234, Address Goes Here</p>
        <p>Country Name, 123456</p>
      </div>
    </div>
  </section>

  <section class="card card-back" aria-label="Card back">
    <div class="back-badge" aria-hidden="true"></div>
    <p class="back-wordmark">Dalvik Ostrander<span class="line-small">PHOTOGRAPHY</span></p>
    <p class="back-web">www.tavorelstudio.com</p>
  </section>
</main>
</body>
</html>
```